Folder outside surface for Gulfview Sight Clinics

Hello :
Attached, please see the images and logo that are meant for a 9x12 inch folder. I need a 300dpi file (png, jpeg, and vector) that fits the diagram from a printing company.

```html
<!DOCTYPE html>
<html lang="en">
<head>
<meta charset="utf-8">
<title>Gulfview Sight Clinics – Folder Outside Surface</title>
<link rel="stylesheet" href="https://fonts.googleapis.com/css2?family=Montserrat:wght@400;800&display=swap">
<style>
  :root {
    --backdrop: #e2e2e2;
    --paper: #f1f1f1;
    --navy: #2a3a6e;
    --navy-deep: #233163;
    --teal: #4e9fa6;
    --orange: #e08e5a;
    --white: #ffffff;
  }
  html, body {
    margin: 0;
    padding: 0;
    width: 1200px;
    height: 1200px;
    overflow: hidden;
    background: var(--backdrop);
  }
  .folder-cover {
    position: absolute;
    left: 187px;
    top: 50px;
    width: 825px;
    height: 1100px;
    background: var(--paper);
    box-shadow: 0 6px 24px rgba(0,0,0,0.12);
    overflow: hidden;
  }
  .cover-shapes {
    position: absolute;
    inset: 0;
    width: 100%;
    height: 100%;
  }
  .brand-lockup {
    position: absolute;
    left: 0;
    right: 0;
    top: 330px;
    display: flex;
    align-items: center;
    justify-content: center;
    gap: 22px;
  }
  .brand-mark {
    width: 56px;
    height: 56px;
    border-radius: 50%;
    background: var(--orange);
    flex: none;
  }
  .brand-name {
    font-family: "Montserrat", sans-serif;
    font-weight: 800;
    font-size: 46px;
    line-height: 1.05;
    color: var(--navy);
    text-transform: uppercase;
    letter-spacing: 0.01em;
    margin: 0;
  }
  .tagline {
    position: absolute;
    left: 70px;
    top: 975px;
    margin: 0;
    font-family: "Montserrat", sans-serif;
    font-weight: 400;
    font-size: 22px;
    line-height: 1.45;
    letter-spacing: 0.22em;
    color: var(--white);
    text-transform: uppercase;
  }
</style>
</head>
<body>
  <main class="folder-cover">
    <svg class="cover-shapes" viewBox="0 0 825 1100" aria-hidden="true">
      <polygon class="accent-orange" points="825,620 825,1100 575,1100" fill="var(--orange)"/>
      <polygon class="accent-teal" points="0,858 605,848 600,858 0,866" fill="var(--teal)"/>
      <polygon class="band-navy" points="0,882 565,882 505,1100 0,1100" fill="var(--navy)"/>
    </svg>

    <div class="brand-lockup">
      <span class="brand-mark"></span>
      <h1 class="brand-name">Gulfview<br>Sight Clinics</h1>
    </div>

    <p class="tagline">Trusted Care<br>Guided by Science</p>
  </main>
</body>
</html>
```